Coral Ridge Pools New website

I currently operate a swimming pool service and repair business and looking for a re design for my website as it has been over 5 years since it was designed. current site is coralridgepoolsqx.com

```html
<!DOCTYPE html>
<html lang="en">
<head>
<meta charset="utf-8">
<title>Coral Ridge Pools</title>
<link href="https://fonts.googleapis.com/css2?family=Montserrat:wght@400;500;600;700;800&family=Yellowtail&display=block" rel="stylesheet">
<style>
:root{
  --navy:#0a4676;
  --card:#0d5489;
  --ink:#0d4b86;
  --orange:#f7a21b;
  --cyan:#17b9ea;
  --text:#1f2f44;
  --muted:#5b6675;
  --white:#ffffff;
}
*{box-sizing:border-box;margin:0;padding:0}
html,body{width:1200px;height:4209px;overflow:hidden}
body{position:relative;background:var(--white);font-family:'Montserrat',sans-serif;color:var(--text)}
.script{font-family:'Yellowtail',cursive;color:var(--orange);font-weight:400}
.btn{position:absolute;display:flex;align-items:center;justify-content:center;gap:6px;border-radius:30px;font-weight:700;font-size:13px;letter-spacing:.3px;color:var(--white);background:var(--cyan);text-decoration:none;text-transform:uppercase}
.btn svg{width:13px;height:13px}
.bg-shapes{position:absolute;left:0;top:0;width:1200px;height:4209px}

/* nav */
.brand{position:absolute;left:84px;top:36px;display:flex;align-items:center;gap:8px;font-weight:800;font-size:18px;color:var(--white)}
.brand .dot{width:22px;height:22px;border-radius:50%;background:var(--orange)}
.nav{position:absolute;top:29px;left:0;width:1200px;height:20px;font-size:14px;font-weight:600;color:var(--white)}
.nav a{position:absolute;color:var(--white);text-decoration:none}
.nav a.active{color:var(--orange)}
.nav-cta{left:929px;top:13px;width:184px;height:49px}

/* hero */
.hero-copy{position:absolute;left:164px;width:874px;text-align:center;color:var(--white)}
.hero-tag{top:258px;font-size:30px;color:var(--orange)}
.hero-title{top:296px;font-size:64px;font-weight:800;line-height:72px;letter-spacing:.5px}
.hero-btn{left:517px;top:544px;width:166px;height:50px;background:transparent;border:2px solid var(--white)}
.slide-no{position:absolute;left:1090px;font-size:14px;font-weight:700;color:var(--white)}
.slide-no.first{top:336px;font-size:24px;font-weight:500;color:var(--orange)}
.slide-bar{position:absolute;left:1111px;top:372px;width:2px;height:112px;background:rgba(255,255,255,.35)}
.slide-bar::before{content:"";position:absolute;left:0;top:0;width:2px;height:28px;background:var(--orange)}

/* estimate */
.estimate{position:absolute;left:147px;top:930px;width:380px;height:468px;background:var(--navy);border-radius:14px;box-shadow:0 8px 0 -3px var(--orange)}
.estimate .script{position:absolute;left:24px;top:34px;font-size:30px}
.estimate h2{position:absolute;left:24px;top:70px;font-size:40px;font-weight:700;color:var(--white)}
.field{position:absolute;left:24px;width:330px;height:46px;border:1.5px solid rgba(255,255,255,.45);border-radius:24px;display:flex;align-items:center;gap:10px;padding-left:16px;font-size:14px;color:rgba(255,255,255,.85)}
.field svg{width:14px;height:14px;stroke:rgba(255,255,255,.85);fill:none;stroke-width:2}
.estimate .btn{left:24px;top:370px;width:330px;height:48px}

/* welcome */
.welcome{position:absolute;left:610px;top:950px;width:520px}
.welcome .script{font-size:38px;display:block;margin-left:2px}
.welcome h2{font-size:50px;font-weight:800;color:var(--ink);margin-top:-2px;line-height:58px}
.lead{font-size:16px;font-weight:600;line-height:26px;color:var(--text);margin:18px 0 0 3px;width:470px}
.rule-text{border-left:2px solid #9fb3c8;padding-left:18px;margin:22px 0 0 3px;font-size:14px;line-height:27px;color:var(--muted);width:480px}
.welcome-btn{left:613px;top:1316px;width:169px;height:48px}

/* services */
.services-head{position:absolute;left:0;width:1200px;text-align:center;color:var(--white)}
.services-head .script{display:block;font-size:40px}
.services-head h2{font-size:50px;font-weight:800}
.svc{position:absolute;left:85px;width:1028px;height:378px;background:var(--card);border-radius:6px}
.svc .photo{position:absolute;top:8px;width:514px;height:362px;border-radius:4px}
.svc .body{position:absolute;top:40px;width:390px;color:var(--white)}
.svc .icon{width:64px;height:58px;border-radius:6px;background:linear-gradient(135deg,rgba(247,162,27,.9),rgba(23,185,234,.8))}
.svc h3{font-size:24px;font-weight:700;margin-top:22px}
.svc p{font-size:14.5px;line-height:24px;margin-top:12px;color:rgba(255,255,255,.92)}
.svc .more{display:inline-flex;align-items:center;gap:5px;margin-top:18px;font-size:13px;font-weight:700;color:var(--cyan);border-bottom:1.5px solid var(--cyan);padding-bottom:2px;text-decoration:none}
.svc .more svg{width:13px;height:13px}

/* why */
.why{position:absolute;left:630px;top:3210px;width:470px}
.why h2{font-size:52px;font-weight:800;color:var(--ink)}
.why .rule-text{margin-top:22px;width:460px}
.why-btn{left:633px;top:3453px;width:168px;height:48px}

/* footer */
.f-brand{position:absolute;left:128px;top:3860px;display:flex;align-items:center;gap:8px;font-weight:800;font-size:18px;color:var(--white)}
.f-brand .dot{width:22px;height:22px;border-radius:50%;background:var(--orange)}
.social{position:absolute;top:3975px;width:22px;height:22px;border:2.5px solid var(--orange);border-radius:4px}
.f-col{position:absolute;top:3822px;color:var(--white)}
.f-col h4{font-size:15px;font-weight:700;color:var(--orange);letter-spacing:.2px}
.f-col h4::after{content:"";display:block;width:26px;height:2px;background:var(--orange);margin-top:8px}
.f-col ul{list-style:none;margin-top:18px}
.f-col li{font-size:13px;line-height:28.5px}
.contact-row{display:flex;align-items:center;gap:12px;font-size:13px;margin-top:14px}
.contact-row:first-of-type{margin-top:18px}
.contact-row .ic{width:32px;height:32px;border-radius:50%;background:var(--cyan);display:flex;align-items:center;justify-content:center}
.contact-row svg{width:15px;height:15px;fill:var(--white)}
.f-rule{position:absolute;left:85px;top:4120px;width:1028px;height:1px;background:rgba(255,255,255,.25)}
.copy{position:absolute;left:85px;top:4154px;font-size:13px;color:rgba(255,255,255,.8)}
.copy span{color:var(--orange)}
</style>
</head>
<body>

<svg class="bg-shapes" viewBox="0 0 1200 4209">
  <defs>
    <linearGradient id="heroGrad" x1="0" y1="0" x2="1" y2="1">
      <stop offset="0" stop-color="#2a7fa6"/>
      <stop offset=".55" stop-color="#4aa3bf"/>
      <stop offset="1" stop-color="#8a8f8c"/>
    </linearGradient>
    <linearGradient id="whyGrad" x1="0" y1="0" x2="1" y2="1">
      <stop offset="0" stop-color="#c9dbe6"/>
      <stop offset=".6" stop-color="#3c8fb0"/>
      <stop offset="1" stop-color="#1c5f86"/>
    </linearGradient>
    <linearGradient id="footGrad" x1="0" y1="0" x2="0" y2="1">
      <stop offset="0" stop-color="#17232e"/>
      <stop offset=".6" stop-color="#0e2234"/>
      <stop offset="1" stop-color="#0b3351"/>
    </linearGradient>
  </defs>

  <!-- hero -->
  <path d="M0,700 Q0,735 34,744 L566,852 Q600,860 634,852 L1166,744 Q1200,735 1200,700" fill="none" stroke="#f7a21b" stroke-width="6"/>
  <path d="M0,0 H1200 V690 Q1200,722 1168,730 L632,836 Q600,843 568,836 L32,730 Q0,722 0,690 Z" fill="url(#heroGrad)" stroke="#0d4b86" stroke-width="6" role="img" aria-label="Photo of a technician cleaning a tiled pool edge"/>
  <rect x="0" y="0" width="1200" height="78" fill="rgba(255,255,255,.12)"/>
  <path d="M602,145 Q602,139 612,147 L1022,410 Q1038,429 1022,448 L612,711 Q602,719 592,711 L180,448 Q164,429 180,410 L592,147 Q602,139 602,145 Z" fill="rgba(13,84,137,.55)" stroke="#0d4b86" stroke-width="14" stroke-linejoin="round"/>
  <path d="M602,145 Q602,139 612,147 L1022,410 Q1038,429 1022,448 L612,711 Q602,719 592,711 L180,448 Q164,429 180,410 L592,147 Q602,139 602,145 Z" fill="none" stroke="#f7a21b" stroke-width="5" stroke-linejoin="round"/>
  <path d="M600,795 L675,845 L600,895 L525,845 Z" fill="#ffffff" stroke="#0d4b86" stroke-width="5" stroke-linejoin="round"/>
  <path d="M600,803 L663,845 L600,887 L537,845 Z" fill="none" stroke="#f7a21b" stroke-width="3" stroke-linejoin="round"/>

  <!-- services band -->
  <path d="M0,1600 Q0,1570 30,1562 L570,1450 Q600,1442 630,1450 L1170,1562 Q1200,1570 1200,1600 V2930 Q1200,2960 1170,2968 L630,3088 Q600,3095 570,3088 L30,2968 Q0,2960 0,2930 Z" fill="none" stroke="#f7a21b" stroke-width="12"/>
  <path d="M0,1600 Q0,1570 30,1562 L570,1450 Q600,1442 630,1450 L1170,1562 Q1200,1570 1200,1600 V2930 Q1200,2960 1170,2968 L630,3088 Q600,3095 570,3088 L30,2968 Q0,2960 0,2930 Z" fill="#0a4676"/>

  <!-- why image -->
  <path d="M337,3180 Q337,3172 347,3178 L578,3332 Q589,3343 578,3354 L347,3508 Q337,3515 327,3508 L96,3354 Q85,3343 96,3332 L327,3178 Q337,3172 337,3180 Z" fill="url(#whyGrad)" stroke="#f7a21b" stroke-width="10" stroke-linejoin="round" role="img" aria-label="Photo of a worker pressure washing an empty pool"/>
  <path d="M337,3186 L572,3343 L337,3500 L102,3343 Z" fill="none" stroke="#0d4b86" stroke-width="4" stroke-linejoin="round"/>

  <!-- footer -->
  <path d="M0,3790 Q0,3760 30,3752 L570,3590 Q600,3581 630,3590 L1170,3752 Q1200,3760 1200,3790 V4209 H0 Z" fill="url(#footGrad)" stroke="#f7a21b" stroke-width="8" role="img" aria-label="Dimmed photo of a pool terrace at night"/>
  <path d="M0,3800 Q0,3772 30,3764 L570,3602 Q600,3594 630,3602 L1170,3764 Q1200,3772 1200,3800" fill="none" stroke="#0d4b86" stroke-width="7"/>
</svg>

<!-- nav -->
<div class="brand"><span class="dot"></span>Coral Ridge Pools</div>
<nav class="nav">
  <a class="active" style="left:514px">Home</a>
  <a style="left:609px">About Us</a>
  <a style="left:729px">Services</a>
  <a style="left:842px">Contact</a>
</nav>
<a class="btn nav-cta">Free Estimate
  <svg viewBox="0 0 14 14"><circle cx="7" cy="7" r="7" fill="#fff"/><path d="M5 4l3 3-3 3" stroke="#17b9ea" stroke-width="2" fill="none"/></svg></a>

<!-- hero -->
<div class="hero-copy hero-tag script">Our full-service pool company</div>
<h1 class="hero-copy hero-title">Proudly Serves<br>The Entire<br>Las Vegas Valley</h1>
<a class="btn hero-btn">Read More
  <svg viewBox="0 0 14 14"><circle cx="7" cy="7" r="7" fill="#fff"/><path d="M5 4l3 3-3 3" stroke="#2a7fa6" stroke-width="2" fill="none"/></svg></a>
<div class="slide-no first">01</div>
<div class="slide-bar"></div>
<div class="slide-no" style="top:492px">04</div>

<!-- estimate -->
<section class="estimate">
  <span class="script">Get a</span>
  <h2>Free Estimate</h2>
  <div class="field" style="top:129px"><svg viewBox="0 0 16 16"><circle cx="8" cy="5" r="3"/><path d="M2 15c0-4 12-4 12 0"/></svg>Name</div>
  <div class="field" style="top:185px"><svg viewBox="0 0 16 16"><rect x="1" y="3" width="14" height="10" rx="1"/><path d="M1 4l7 5 7-5"/></svg>Email</div>
  <div class="field" style="top:241px"><svg viewBox="0 0 16 16"><path d="M3 1h3l1 4-2 1c1 2 3 4 5 5l1-2 4 1v3c0 1-1 2-2 2C7 15 1 9 1 3c0-1 1-2 2-2z"/></svg>Phone</div>
  <div class="field" style="top:296px"><svg viewBox="0 0 16 16"><path d="M2 14l1-4 8-8 3 3-8 8z"/></svg>Please explain your needs</div>
  <a class="btn">Get Your Fee Estimate
    <svg viewBox="0 0 14 14"><circle cx="7" cy="7" r="7" fill="#fff"/><path d="M5 4l3 3-3 3" stroke="#17b9ea" stroke-width="2" fill="none"/></svg></a>
</section>

<!-- welcome -->
<section class="welcome">
  <span class="script">Welcome to</span>
  <h2>Coral Ridge Pools</h2>
  <p class="lead">When you need professional pool cleaning services in Nevada, you can count on the professionals at Coral Ridge Pools to provide</p>
  <p class="rule-text">You with superior and prompt solutions. Whether you need assistance with a residential or commercial pool, we’ll vacuum, brush, and thoroughly clean your pool so it’s swim-ready. We’ll also clean your pool filters and inform you of any issues that arise.</p>
</section>
<a class="btn welcome-btn">Read More
  <svg viewBox="0 0 14 14"><circle cx="7" cy="7" r="7" fill="#fff"/><path d="M5 4l3 3-3 3" stroke="#17b9ea" stroke-width="2" fill="none"/></svg></a>

<!-- services -->
<div class="services-head" style="top:1562px"><span class="script">Our</span></div>
<div class="services-head" style="top:1606px"><h2>Services</h2></div>

<article class="svc" style="top:1704px">
  <div class="body" style="left:68px">
    <div class="icon" role="img" aria-label="Pool cleaner icon"></div>
    <h3>Pool Services</h3>
    <p>When you invested in your pool, you knew it was a long-term investment in both money and time. At home, it’s an oasis, a place to beat the heat and relax. At your business, it’s both an accessory for the enjoyment of your clients as well as</p>
    <a class="more">READ MORE <svg viewBox="0 0 14 14"><circle cx="7" cy="7" r="7" fill="#17b9ea"/><path d="M5 4l3 3-3 3" stroke="#fff" stroke-width="2" fill="none"/></svg></a>
  </div>
  <div class="photo" style="left:508px;background:linear-gradient(180deg,#3c6b3a 0%,#c9c9c4 38%,#2d9fd0 60%,#1a7fbf 100%)" role="img" aria-label="Photo of a technician vacuuming a pool beside lounge chairs"></div>
</article>

<article class="svc" style="top:2108px">
  <div class="photo" style="left:8px;background:linear-gradient(180deg,#4a5b4a 0%,#e9e4dc 35%,#2d2f33 48%,#2bb5e8 58%,#13a6e0 100%)" role="img" aria-label="Photo of a hotel pool lined with cabanas"></div>
  <div class="body" style="left:598px">
    <div class="icon" role="img" aria-label="Commercial building icon"></div>
    <h3>Commercial Pool</h3>
    <p>As a commercial property owner or manager, doing your job well requires you to be mindful of all the details. Every day is filled with a thousand different decisions, and when you need support for your facility  it’s critical that the company you rely upon</p>
    <a class="more">READ MORE <svg viewBox="0 0 14 14"><circle cx="7" cy="7" r="7" fill="#17b9ea"/><path d="M5 4l3 3-3 3" stroke="#fff" stroke-width="2" fill="none"/></svg></a>
  </div>
</article>

<article class="svc" style="top:2511px">
  <div class="body" style="left:68px">
    <div class="icon" role="img" aria-label="Pool ladder icon"></div>
    <h3>Residential Pool</h3>
    <p>Here in Southern Nevada, you know it can get really, really hot. That’s why you invested in your pool at home; so that you would always have a place to cool off and relax with family and friends. You want your pool to look its best and function</p>
    <a class="more">READ MORE <svg viewBox="0 0 14 14"><circle cx="7" cy="7" r="7" fill="#17b9ea"/><path d="M5 4l3 3-3 3" stroke="#fff" stroke-width="2" fill="none"/></svg></a>
  </div>
  <div class="photo" style="left:508px;background:linear-gradient(160deg,#1f2a1c 0%,#8a6a3f 35%,#3aa6c9 62%,#1689bd 100%)" role="img" aria-label="Photo of a residential pool lit at dusk"></div>
</article>

<!-- why -->
<section class="why">
  <h2>Why Choose Us?</h2>
  <p class="rule-text">Our full-service pool company proudly serves the entire Las Vegas valley, and we’re certified by the Desert Basin Water Safety Board to maintain the highest level of pool safety. If you need repairs, maintenance, scheduled cleanings, or any other pool services, contact us online or by phone today.</p>
</section>
<a class="btn why-btn">Contact Us
  <svg viewBox="0 0 14 14"><circle cx="7" cy="7" r="7" fill="#fff"/><path d="M5 4l3 3-3 3" stroke="#17b9ea" stroke-width="2" fill="none"/></svg></a>

<!-- footer -->
<div class="f-brand"><span class="dot"></span>Coral Ridge Pools</div>
<span class="social" style="left:158px"></span>
<span class="social" style="left:197px"></span>
<span class="social" style="left:233px"></span>

<div class="f-col" style="left:360px">
  <h4>QUICK LINKS</h4>
  <ul><li>Home</li><li>About Us</li><li>Our Services</li><li>Free Estimate</li><li>Blog</li><li>Contact</li><li>Privacy Policy</li></ul>
</div>
<div class="f-col" style="left:575px">
  <h4>SERVICES</h4>
  <ul><li>Pool Services</li><li>Commercial Pool</li><li>Residential Pool</li></ul>
</div>
<div class="f-col" style="left:806px">
  <h4>CONTACT INFO</h4>
  <div class="contact-row"><span class="ic"><svg viewBox="0 0 16 16"><path d="M3 1h3l1 4-2 1c1 2 3 4 5 5l1-2 4 1v3c0 1-1 2-2 2C7 15 1 9 1 3c0-1 1-2 2-2z"/></svg></span>(702) 555-0148</div>
  <div class="contact-row"><span class="ic"><svg viewBox="0 0 16 16"><path d="M1 3h14v10H1z M1 3l7 6 7-6"/></svg></span>hello@coralridgepoolsqx.com</div>
</div>
<div class="f-rule"></div>
<p class="copy">© 2026 <span>Coral Ridge Pools</span>. All right reserved.</p>

</body>
</html>
```